Need Help having my business card stand out

I am the owner of Pine Ridge Canine Coaching and would like for my business cards to stand out. I have been trying to keep designing them myself but I can't get what I have in my head on the card. I will try my best to post templates that I like for inspirations. I want something unique but elegant. I don't want in to look cartoony or cheesy. It needs to pop in a pet shop but also in a coffee shop or gym.

Target Market(s)

Dog owners, Married ,No young kids Jr High school kids and up (maybe kids on the way) Executives, Stay at home moms/wives, Small business owners

Industry/Entity Type

Dog Training

Contact Information for Business Card

Trevor Holloway, 555-304-7162, info@pineridgecanine.example, www.pineridgecanine.example

Colors

Designer to choose colors to be used in the design.

Requirements
Must have
• my logo
Should not have
• Cursive lettering

```html
<!DOCTYPE html>
<html lang="en">
<head>
<meta charset="utf-8">
<title>Pine Ridge Canine Coaching – Business Card</title>
<link rel="stylesheet" href="https://fonts.googleapis.com/css2?family=Arvo:ital,wght@0,700;1,700&display=swap">
<style>
  :root {
    --page: #ececec;
    --cyan: #38bfd6;
    --charcoal: #2e2e30;
    --white: #ffffff;
    --shadow: rgba(0, 0, 0, 0.18);
  }
  * { box-sizing: border-box; margin: 0; padding: 0; }
  html, body {
    width: 1200px;
    height: 960px;
    overflow: hidden;
    background: var(--page);
  }
  .sheet {
    width: 1200px;
    height: 960px;
    display: flex;
    flex-direction: column;
    align-items: center;
    justify-content: center;
    gap: 60px;
  }
  .card {
    position: relative;
    width: 700px;
    height: 400px;
    background: var(--cyan);
    box-shadow: 0 10px 30px var(--shadow);
    overflow: hidden;
    color: var(--white);
    font-family: "Arvo", Georgia, serif;
  }

  /* Contact side */
  .card-contact .brand-panel {
    position: absolute;
    inset: 0;
    background: var(--charcoal);
    clip-path: polygon(62% 0, 100% 0, 100% 100%, 40% 100%);
  }
  .card-contact .holder-name {
    position: absolute;
    left: 80px;
    top: 62px;
    font-size: 40px;
    font-weight: 700;
    letter-spacing: 0.5px;
  }
  .card-contact .contact-list {
    position: absolute;
    left: 44px;
    top: 170px;
    list-style: none;
    display: flex;
    flex-direction: column;
    gap: 20px;
  }
  .contact-item {
    display: flex;
    align-items: center;
    gap: 14px;
    font-size: 18px;
    font-style: italic;
    font-weight: 700;
  }
  .contact-item svg { width: 20px; height: 20px; flex: none; }
  .card-contact .brand-name {
    position: absolute;
    right: 40px;
    top: 150px;
    width: 230px;
    text-align: center;
    font-size: 28px;
    font-weight: 700;
    line-height: 1.25;
    color: var(--white);
  }

  /* Logo side */
  .card-logo {
    display: flex;
    align-items: center;
    justify-content: center;
    gap: 24px;
  }
  .card-logo .brand-mark {
    width: 64px;
    height: 64px;
    border-radius: 50%;
    background: var(--white);
    flex: none;
  }
  .card-logo .brand-name {
    font-size: 46px;
    font-weight: 700;
    line-height: 1.15;
  }
</style>
</head>
<body>
<main class="sheet">

  <section class="card card-contact" aria-label="Business card, contact side">
    <div class="brand-panel"></div>
    <h1 class="holder-name">Trevor Holloway</h1>
    <ul class="contact-list">
      <li class="contact-item">
        <svg viewBox="0 0 24 24" aria-hidden="true"><path fill="#fff" d="M6.6 10.8a15 15 0 0 0 6.6 6.6l2.2-2.2c.3-.3.7-.4 1-.2 1.1.4 2.3.6 3.6.6.6 0 1 .4 1 1V20c0 .6-.4 1-1 1A17 17 0 0 1 3 4c0-.6.4-1 1-1h3.5c.6 0 1 .4 1 1 0 1.3.2 2.5.6 3.6.1.3 0 .7-.2 1z"/></svg>
        <span>555-304-7162</span>
      </li>
      <li class="contact-item">
        <svg viewBox="0 0 24 24" aria-hidden="true"><rect x="2.5" y="5" width="19" height="14" fill="none" stroke="#fff" stroke-width="1.8"/><path d="M2.5 5l9.5 8 9.5-8" fill="none" stroke="#fff" stroke-width="1.8"/></svg>
        <span>info@pineridgecanine.example</span>
      </li>
      <li class="contact-item">
        <svg viewBox="0 0 24 24" aria-hidden="true"><g fill="none" stroke="#fff" stroke-width="1.6"><circle cx="12" cy="12" r="9"/><ellipse cx="12" cy="12" rx="4" ry="9"/><path d="M3 12h18M5 7h14M5 17h14"/></g></svg>
        <span>www.pineridgecanine.example</span>
      </li>
    </ul>
    <p class="brand-name">Pine Ridge Canine Coaching</p>
  </section>

  <section class="card card-logo" aria-label="Business card, logo side">
    <span class="brand-mark" aria-hidden="true"></span>
    <p class="brand-name">Pine Ridge<br>Canine Coaching</p>
  </section>

</main>
</body>
</html>
```